Plakat-Design für Vermieter von Ferienwohnungen im Allgäu
Zielgruppe
Wir vermieten Ferienwohnungen im Allgäu.
www.residenz-wiesental.de
Aufgabenstellung
Das Schild (Querformat) sollte freundlich, ansprechend und modern sein. Größe 140x180 cm.
Es wird eine Begrüßung für den Gast, wenn er in die Tiefgarage fährt.
Text:
Herzlich Willkommen
in der Residenz Lerchenau
Als Hintergrund können wir uns Berge, Landschaft oder ähnliches vorstellen.

```html
<!DOCTYPE html>
<html lang="de">
<head>
<meta charset="utf-8">
<title>Herzlich Willkommen – Residenz Lerchenau</title>
<link href="https://fonts.googleapis.com/css2?family=Playball&display=swap" rel="stylesheet">
<style>
  :root {
    --page: #ffffff;
    --brand-red: #a7302b;
    --ink: #111111;
    --sun: #f2b720;
    --veil: rgba(255, 255, 255, 0.82);
    --sky: #f4f6f8;
    --meadow-light: #c9c58a;
    --meadow-dark: #7d8a3c;
  }
  html, body {
    margin: 0;
    width: 1200px;
    height: 951px;
    overflow: hidden;
    background: var(--page);
  }
  .poster {
    position: absolute;
    left: 48px;
    top: 48px;
    width: 1104px;
    height: 858px;
    overflow: hidden;
    box-shadow: 0 0 24px rgba(0, 0, 0, 0.18);
    font-family: "Playball", cursive;
  }
  .backdrop {
    position: absolute;
    inset: 0;
    background:
      linear-gradient(90deg, rgba(120, 105, 90, 0.55) 0%, rgba(120, 105, 90, 0.15) 28%, rgba(255, 255, 255, 0) 45%, rgba(255, 255, 255, 0) 75%, rgba(40, 40, 40, 0.35) 90%, rgba(40, 60, 35, 0.5) 100%),
      linear-gradient(180deg, var(--sky) 0%, #eef0ef 55%, var(--meadow-light) 78%, var(--meadow-dark) 100%);
  }
  .welcome-disc {
    position: absolute;
    left: 176px;
    top: 54px;
    width: 752px;
    height: 752px;
    border-radius: 50%;
    background: var(--veil);
  }
  .brand {
    position: absolute;
    top: 108px;
    left: 0;
    width: 1104px;
    display: flex;
    justify-content: center;
    align-items: center;
    gap: 14px;
  }
  .brand-dot {
    width: 52px;
    height: 52px;
    border-radius: 50%;
    background: var(--sun);
  }
  .brand-name {
    font-size: 40px;
    color: var(--brand-red);
    line-height: 1;
  }
  .headline {
    position: absolute;
    left: 0;
    width: 1104px;
    margin: 0;
    text-align: center;
    color: var(--brand-red);
    font-weight: 400;
    font-size: 140px;
    line-height: 1;
  }
  .headline-first { top: 250px; }
  .headline-second { top: 392px; }
  .subline {
    position: absolute;
    left: 0;
    width: 1104px;
    margin: 0;
    text-align: center;
    color: var(--ink);
    font-size: 70px;
    line-height: 1;
  }
  .subline-first { top: 560px; }
  .subline-second { top: 648px; }
</style>
</head>
<body>
  <main class="poster">
    <div class="backdrop" role="img" aria-label="Foto: neugierige Kühe auf einer sonnigen Allgäuer Wiese"></div>
    <div class="welcome-disc"></div>

    <div class="brand">
      <span class="brand-dot"></span>
      <span class="brand-name">Residenz Wiesental</span>
    </div>

    <h1 class="headline headline-first">Herzlich</h1>
    <p class="headline headline-second">Willkommen</p>

    <p class="subline subline-first">in Ihrer Residenz</p>
    <p class="subline subline-second">Lerchenau</p>
  </main>
</body>
</html>
```